IT Van Re-Design

I currently have an onsite service IT van that the signage is getting old and faded. I am looking for a fresh look, all sides, fresh professional eye catching design that depicts a modern computer service centre. I don't really like the current design and would like something that will be memorable and eye catching. I don't mind the colours though.
I am open to suggestions, something that is humorous would be considered as well as something that is appealing on the more serious/Professional side.
The design that appeals to me best would be the one I will select.
our web site is www.pelmarit.com.au for more details on what we do. (This is to be updated, but this is a later project).
Current van design has many services such as Fibre, Alarm Surveillance etc. I will remove most of these, depending on the design layout I will select the wording to add to the design layout as I analyse what I will remove and keep.
I want the design to mainly focus around IT rather than Alarms for example, this is the core of our business and the other items are additional services that we do.
I have also attached the current van pictures as an FYI. The van is a Varnesse Tolquin.
Looking forward to some ideas!
Updates
I have just updated two photos with dimensions. Please let me know if anything is unclear.
Project Deadline Extended
Reason: Thank you for the designers that have submitted designs. I would like to extend the deadline as we are currently on holidays and I would like to get feedback from my colleagues before deciding.
I will be providing feedback to the current designs shortly.
thanks again
Project Deadline Extended
Reason: Thank you all for the designs so far. I am unable to provide feebdack to all designers currently as I am away on vacation and has been extended until the 13th January with limited internet connectivity.
I will be monitoring this page more frequently in the coming days.
thanks again
Target Market(s)
Small/Medium Business then home users are our main customer base.
Industry/Entity Type
Computer
Look and feel

```html
<!DOCTYPE html>
<html lang="en">
<head>
<meta charset="utf-8">
<title>Pelmarit Van Wrap Layout</title>
<link href="https://fonts.googleapis.com/css2?family=Arimo:wght@400;700&family=Nunito:wght@600&display=swap" rel="stylesheet">
<style>
  :root{
    --paper:#ffffff;
    --frame:#d9d9d9;
    --navy:#1530a0;
    --brand-blue:#1e3a9e;
    --royal:#2a3fbf;
    --violet:#6a68e8;
    --sky:#5fa0f5;
    --alert-red:#cc0000;
    --magenta:#cc10d8;
    --ink:#111111;
    --window:#1c1c1c;
    --phone:#7b6cf0;
  }
  html,body{margin:0;padding:0;width:1200px;height:1200px;overflow:hidden;background:var(--paper);}
  .sheet{position:relative;width:1200px;height:1200px;box-sizing:border-box;border:1px solid var(--frame);}
  .sheet svg{display:block;}
  .brand{font-family:"Nunito",sans-serif;font-weight:600;fill:var(--brand-blue);}
  .body-text{font-family:"Arimo",sans-serif;}
  .bold{font-weight:700;}
  .service-blue{fill:var(--navy);}
  .service-red{fill:var(--alert-red);}
</style>
</head>
<body>
<div class="sheet">
<svg width="1198" height="1198" viewBox="0 0 1200 1200" xmlns="http://www.w3.org/2000/svg">
  <defs>
    <linearGradient id="sweepBlue" x1="0" y1="0" x2="0" y2="1">
      <stop offset="0" stop-color="#2a3fbf"/>
      <stop offset="1" stop-color="#6a68f2"/>
    </linearGradient>
    <linearGradient id="sweepViolet" x1="0" y1="0" x2="1" y2="1">
      <stop offset="0" stop-color="#6d66cc"/>
      <stop offset="0.6" stop-color="#4f5ff0"/>
      <stop offset="1" stop-color="#6a68f2"/>
    </linearGradient>
    <linearGradient id="rearPurple" x1="0" y1="0" x2="1" y2="0">
      <stop offset="0" stop-color="#1e2fa8"/>
      <stop offset="1" stop-color="#cc10d8"/>
    </linearGradient>
    <linearGradient id="badgeSilver" x1="0" y1="0" x2="0" y2="1">
      <stop offset="0" stop-color="#f2f2f2"/>
      <stop offset="0.5" stop-color="#c9c9c9"/>
      <stop offset="1" stop-color="#e6e6e6"/>
    </linearGradient>
    <linearGradient id="circuitTone" x1="0" y1="0" x2="1" y2="0">
      <stop offset="0" stop-color="#3a2a8a"/>
      <stop offset="0.5" stop-color="#b030c8"/>
      <stop offset="1" stop-color="#5a2aa0"/>
    </linearGradient>
    <clipPath id="hoodClip">
      <path d="M215,87 Q367,80 520,87 L520,296 L482,298 L472,334 L260,335 L250,298 L215,296 Z"/>
    </clipPath>
    <clipPath id="rearClip"><rect x="575" y="75" width="396" height="263"/></clipPath>
    <clipPath id="sideLeftClip"><rect x="225" y="405" width="332" height="288" rx="32"/></clipPath>
    <clipPath id="sideRightClip"><rect x="625" y="405" width="330" height="288" rx="32"/></clipPath>
  </defs>

  <!-- Bonnet panel -->
  <g class="panel-bonnet" clip-path="url(#hoodClip)">
    <rect x="215" y="80" width="305" height="260" fill="#fff"/>
    <path d="M215,87 L236,87 Q248,250 335,340 L215,340 Z" fill="url(#sweepBlue)"/>
    <path d="M244,87 Q258,245 340,340" fill="none" stroke="var(--sky)" stroke-width="6"/>
    <path d="M425,87 Q475,170 445,232 Q410,300 335,340 L520,340 L520,87 Z" fill="url(#sweepViolet)"/>
    <path d="M455,87 Q510,190 450,280 Q420,318 380,340" fill="none" stroke="#fff" stroke-width="7"/>
  </g>
  <path d="M215,87 Q367,80 520,87 L520,296 L482,298 L472,334 L260,335 L250,298 L215,296 Z" fill="none" stroke="#cfcfcf" stroke-width="1"/>
  <text class="brand" x="368" y="190" font-size="30" text-anchor="middle">PELMARIT</text>
  <rect x="308" y="248" width="122" height="34" rx="3" fill="url(#badgeSilver)" stroke="#9fd8e8" stroke-dasharray="3 2"/>
  <text class="brand" x="369" y="266" font-size="15" text-anchor="middle">PELMARIT</text>
  <text class="body-text bold" x="369" y="277" font-size="7.5" text-anchor="middle" fill="var(--navy)">Computer &amp; Network Services</text>

  <!-- Rear door panel -->
  <g class="panel-rear" clip-path="url(#rearClip)">
    <rect x="575" y="75" width="396" height="263" fill="#fff"/>
    <path d="M575,75 L598,75 Q630,245 765,338 L575,338 Z" fill="url(#sweepBlue)"/>
    <path d="M606,75 Q645,240 770,338" fill="none" stroke="var(--sky)" stroke-width="6"/>
    <path d="M812,75 Q895,140 885,220 Q865,300 785,338 L971,338 L971,75 Z" fill="url(#sweepViolet)"/>
    <path d="M852,75 Q945,180 870,300 Q850,322 825,338" fill="none" stroke="#fff" stroke-width="8"/>
  </g>
  <text class="brand" x="775" y="190" font-size="30" text-anchor="middle">PELMARIT</text>
  <rect x="697" y="242" width="158" height="44" rx="3" fill="url(#badgeSilver)" stroke="#9fd8e8" stroke-dasharray="3 2"/>
  <text class="brand" x="776" y="266" font-size="19" text-anchor="middle">PELMARIT</text>
  <text class="body-text bold" x="776" y="280" font-size="9.5" text-anchor="middle" fill="var(--navy)">Computer &amp; Network Services</text>

  <!-- Side window panel, brand -->
  <g class="panel-side-brand" clip-path="url(#sideLeftClip)">
    <rect x="225" y="405" width="332" height="288" fill="#fff"/>
    <path d="M470,405 Q548,430 548,520 Q548,585 520,612 Q557,590 557,540 L557,405 Z" fill="url(#sweepBlue)"/>
    <path d="M500,405 Q560,450 545,545" fill="none" stroke="#fff" stroke-width="8"/>
    <path d="M225,588 Q300,645 420,648 Q520,645 557,598 L557,693 L225,693 Z" fill="url(#sweepBlue)"/>
    <path d="M228,630 Q320,690 455,695" fill="none" stroke="#fff" stroke-width="7"/>
    <path d="M462,695 Q520,665 557,650" fill="none" stroke="#fff" stroke-width="7"/>
  </g>
  <rect x="225" y="405" width="332" height="288" rx="32" fill="none" stroke="#e4efd8" stroke-width="1"/>
  <text class="brand" x="391" y="528" font-size="44" text-anchor="middle">PELMARIT</text>
  <text class="body-text bold" x="388" y="566" font-size="28" text-anchor="middle" fill="var(--ink)">Computer &amp;</text>
  <text class="body-text bold" x="388" y="587" font-size="15" text-anchor="middle" fill="var(--ink)">Network Services</text>

  <!-- Side window panel, services -->
  <g class="panel-side-services" clip-path="url(#sideRightClip)">
    <rect x="625" y="405" width="330" height="288" fill="url(#sweepBlue)"/>
    <path d="M648,412 Q640,520 655,690 L960,690 L960,412 Z" fill="#fff"/>
    <path d="M640,585 Q760,690 955,600 L955,693 L640,693 Z" fill="url(#sweepViolet)" opacity="0.85"/>
    <rect x="640" y="420" width="300" height="255" rx="26" fill="rgba(240,240,255,0.72)" stroke="#7070f0" stroke-width="1"/>
  </g>
  <g class="service-list body-text bold" font-size="16">
    <circle cx="640" cy="456" r="5" fill="#fff" stroke="#000" stroke-width="1.5"/>
    <text class="service-blue" x="654" y="462">Repairs &amp; Upgrades</text>
    <circle cx="640" cy="488" r="5" fill="#fff" stroke="#000" stroke-width="1.5"/>
    <text class="service-red" x="654" y="494">Servers &amp; Networking</text>
    <circle cx="640" cy="520" r="5" fill="#fff" stroke="#000" stroke-width="1.5"/>
    <text class="service-blue" x="654" y="526">Phone,Data &amp; Fiber Optic Cabling</text>
    <circle cx="640" cy="552" r="5" fill="#fff" stroke="#000" stroke-width="1.5"/>
    <text class="service-red" x="654" y="558">VOIP Telephone Systems</text>
    <circle cx="640" cy="584" r="5" fill="#fff" stroke="#000" stroke-width="1.5"/>
    <text class="service-blue" x="654" y="590">Surveillance Camera Systems</text>
    <text class="service-blue" x="654" y="622">&amp; Alarm Systems</text>
    <circle cx="640" cy="648" r="5" fill="#fff" stroke="#000" stroke-width="1.5"/>
    <text class="service-red" x="654" y="654">Business &amp; Residential</text>
  </g>

  <!-- Van side -->
  <g class="van-side">
    <path d="M218,1002 L218,985 Q226,963 272,950 Q335,934 412,924 Q472,852 542,822 Q605,800 700,795 L930,788 Q966,792 975,850 L978,1002 Z" fill="#fff" stroke="#d9a3d9" stroke-width="1"/>
    <path d="M880,790 L930,788 Q966,792 975,850 L978,1002 L780,1002 Q830,930 925,915 Q942,900 942,842 Q935,815 895,812 Z" fill="url(#rearPurple)"/>
    <rect x="828" y="815" width="112" height="100" rx="14" fill="#f2f2f4"/>
    <text class="brand" x="884" y="870" font-size="17" text-anchor="middle">PELMARIT</text>
    <path d="M445,925 Q470,860 522,835 Q572,824 626,826 Q636,830 633,846 L626,924 Q621,935 606,935 L456,935 Q445,935 445,925 Z" fill="var(--window)"/>
    <path d="M218,1002 L978,1002 L978,1060 Q962,1070 942,1070 Q932,1008 880,1006 Q826,1008 816,1068 L412,1086 Q402,1006 345,1004 Q290,1006 282,1070 Q240,1075 222,1040 Z" fill="#000"/>
    <rect x="412" y="1038" width="404" height="46" fill="url(#circuitTone)" role="img" aria-label="Circuit board pattern strip in purple and blue tones"/>
    <circle cx="345" cy="1064" r="62" fill="#fff"/>
    <circle cx="345" cy="1064" r="56" fill="#fff" stroke="#000" stroke-width="4"/>
    <circle cx="880" cy="1062" r="62" fill="#fff"/>
    <circle cx="880" cy="1062" r="56" fill="#fff" stroke="#000" stroke-width="4"/>

    <text class="brand" x="526" y="964" font-size="14" text-anchor="middle">PELMARIT</text>
    <text class="body-text" x="528" y="973" font-size="7" text-anchor="middle" fill="var(--navy)">Computer &amp; Network Services</text>
    <text class="body-text" x="526" y="988" font-size="11" text-anchor="middle" fill="var(--alert-red)">www.pelmarit.com.au</text>

    <text class="brand" x="730" y="840" font-size="15" text-anchor="middle">PELMARIT</text>
    <text class="body-text" x="731" y="850" font-size="9" text-anchor="middle" fill="var(--navy)">Computer &amp; Network Services</text>
    <text class="body-text" x="730" y="866" font-size="11" text-anchor="middle" fill="var(--phone)">93105847</text>
    <g class="body-text" font-size="8.5" fill="var(--ink)">
      <text x="669" y="887">Repairs &amp; Upgrades</text>
      <text x="669" y="904">Servers &amp; Networking</text>
      <text x="669" y="921">Phone,Data &amp; Fiber Optic Cabling</text>
      <text x="669" y="938">VOIP Telephone Systems</text>
      <text x="669" y="955">Surveillance Camera Systems</text>
      <text x="669" y="972">&amp; Alarm Systems</text>
      <text x="669" y="989">Business &amp; Residential</text>
    </g>
  </g>
</svg>
</div>
</body>
</html>
```